DeskWizard.dk Frontpage design

I'm in the process of starting a It-course website, based in Denmark. The web site Url is - www.deskwizard.dk

The services are:
- Online courses (This is the main service and the most important)
- One to One courses
- Webinar

I need a frontpage design a simple design, but it must shows professionalism. I have no preference in color, but I like white space.

In Denmark the established competitors are:
- www.tasniva.dk (Biggest competitor)
- www.bramfeldt.dk/online-kurser
- www.velunda.dk

Target Market(s)

Mainly companies (B to B), but there are also a small number of private customers

Industry/Entity Type

Online it courses and one to one consulting

Number of Pages Required

1 page

Font styles to use
Sans Serif

Requirements
Must have
• A professional design, white space

```html
<!DOCTYPE html>
<html lang="en">
<head>
<meta charset="utf-8">
<title>DeskWizard.dk – IT courses</title>
<link href="https://fonts.googleapis.com/css2?family=Open+Sans:wght@400;600;700&family=Saira+Semi+Condensed:wght@600;700&display=swap" rel="stylesheet">
<style>
  :root{
    --blue:#0b6fb8;
    --orange:#f89d55;
    --ink:#222831;
    --sky:#e8f4fc;
    --sky-deep:#cfe6f6;
    --white:#ffffff;
    --line:#9aa3ab;
  }
  *{box-sizing:border-box;margin:0;padding:0}
  html,body{width:1200px;height:1185px;overflow:hidden;background:var(--white)}
  body{position:relative;font-family:"Open Sans",sans-serif;color:var(--ink)}
  .abs{position:absolute}
  .display{font-family:"Saira Semi Condensed",sans-serif;font-weight:700;color:var(--blue)}
  .btn{position:absolute;display:flex;align-items:center;justify-content:center;border-radius:4px;
       font-family:"Open Sans",sans-serif;font-weight:700;color:var(--white);text-decoration:none;
       box-shadow:0 2px 4px rgba(0,0,0,.18)}
  .btn--orange{background:var(--orange)}
  .btn--blue{background:var(--blue)}

  /* header */
  .brand{display:flex;align-items:center;gap:8px}
  .brand__dot{width:22px;height:22px;border-radius:50%;background:var(--orange)}
  .brand__name{font-family:"Saira Semi Condensed",sans-serif;font-weight:700;color:var(--blue);font-size:38px;line-height:1}
  .nav{top:45px;left:548px;display:flex;gap:21px;font-size:10.5px;font-weight:700;color:var(--blue)}
  .nav span{display:flex;align-items:center;gap:3px}

  /* hero */
  .hero__art{left:219px;top:122px;width:415px;height:281px;border-radius:4px;
    background:linear-gradient(135deg,var(--sky) 0%,#fbd9bb 55%,#d9d9d9 100%)}
  .hero__title{left:662px;top:152px;font-size:31px;line-height:38px;letter-spacing:.5px}
  .hero__title em{font-style:normal;color:var(--orange)}
  .hero__text{left:662px;top:240px;width:270px;font-size:15px;line-height:24px}

  /* courses */
  .section-title{font-size:22px;line-height:1}
  .card{position:absolute;top:436px;height:166px;background:var(--white);border-radius:4px;
        box-shadow:0 1px 5px rgba(0,0,0,.16);overflow:hidden}
  .card__title{position:absolute;left:11px;top:10px;width:128px;font-size:14.5px;line-height:17px}
  .card__text{position:absolute;left:11px;top:50px;width:130px;font-size:9.5px;line-height:15px;z-index:2}
  .card__art{position:absolute;right:0;top:56px;width:56px;height:84px;border-radius:3px 0 0 3px}
  .card__link{position:absolute;left:0;right:0;bottom:5px;text-align:center;font-size:8.5px;font-weight:700;color:var(--blue)}
  .fade-left{background:linear-gradient(90deg,#fff 0%,rgba(255,255,255,0) 100%)}
  .arrow{position:absolute;width:25px;height:25px;border:1.3px solid var(--ink);border-radius:50%;
         background:var(--white);display:flex;align-items:center;justify-content:center}

  /* styles */
  .mode{position:absolute;top:669px;height:78px;border-radius:3px}
  .mode__label{position:absolute;top:754px;font-size:13px;text-align:center}

  /* footer */
  .footer{left:0;top:963px;width:1200px;height:222px;background:var(--sky)}
  .social{display:flex;gap:13px}
  .social span{width:20px;height:20px;border-radius:50%;background:var(--blue)}
  .news__title{font-family:"Saira Semi Condensed",sans-serif;font-weight:600;color:var(--orange);font-size:12px}
  .news__field{width:175px;border-bottom:1px solid var(--ink);font-size:8.5px;color:#444;padding:0 0 1px 4px}
  .links{font-size:10px;line-height:18.2px}
  .links b{color:var(--blue);font-weight:700}
</style>
</head>
<body>

<header>
  <div class="abs brand" style="left:231px;top:33px">
    <span class="brand__dot"></span>
    <span class="brand__name">DeskWizard</span>
  </div>
  <nav class="abs nav">
    <span>Services
      <svg width="8" height="6" viewBox="0 0 8 6"><path d="M1 1l3 3 3-3" fill="none" stroke="#0b6fb8" stroke-width="1.5"/></svg>
    </span>
    <span>Blog</span>
    <span>About</span>
  </nav>
  <div class="abs" style="left:849px;top:45px;font-size:10.5px;font-weight:700;color:var(--blue)">Sign in</div>
  <a class="btn btn--orange" style="left:899px;top:42px;width:74px;height:20px;font-size:10.5px">Sign up</a>
</header>

<section class="hero">
  <div class="abs hero__art" role="img" aria-label="Illustration of a person on a stool working on a laptop in front of a large browser window"></div>
  <h1 class="abs display hero__title">START YOUR <em>IT</em> CAREER<br>THE EASY WAY</h1>
  <p class="abs hero__text">It is as easy as opening your web browser!</p>
  <a class="btn btn--orange" style="left:662px;top:311px;width:132px;height:28px;font-size:13px">Start today!</a>
</section>

<section class="courses">
  <h2 class="abs display section-title" style="left:265px;top:471px">Broaden your knowledge</h2>
  <p class="abs" style="left:265px;top:509px;font-size:15px">Wide selection of courses.</p>
  <a class="btn btn--blue" style="left:264px;top:555px;width:157px;height:27px;font-size:13px">See all courses</a>

  <div class="card" style="left:534px;width:42px">
    <div class="card__art" style="width:30px;background:linear-gradient(180deg,#f7e3a3,#e8b866)" role="img" aria-label="Course artwork"></div>
    <div class="abs fade-left" style="inset:0;z-index:3"></div>
  </div>

  <article class="card" style="left:588px;width:147px">
    <h3 class="card__title display">Lumen BI in one hour</h3>
    <p class="card__text">Get an introduction to Lumen BI to kickstart your work!</p>
    <div class="card__art" style="background:linear-gradient(180deg,#f7e3a3,#e8b866)" role="img" aria-label="Golden bar chart artwork for the Lumen BI course"></div>
    <div class="card__link">See details
      <svg width="6" height="9" viewBox="0 0 6 9" style="vertical-align:-1px"><path d="M1 1l3.5 3.5L1 8" fill="none" stroke="#0b6fb8" stroke-width="1.3"/></svg>
    </div>
  </article>

  <article class="card" style="left:747px;width:147px">
    <h3 class="card__title display">Serpa for Gridly users</h3>
    <p class="card__text">Get an introduction to Serpa in order to use it in your Gridly workflow!</p>
    <div class="card__art" style="width:84px;background:linear-gradient(135deg,#a7e0c2,#3f9d6a)" role="img" aria-label="Green spreadsheet artwork for the Serpa course"></div>
    <div class="card__link">See details
      <svg width="6" height="9" viewBox="0 0 6 9" style="vertical-align:-1px"><path d="M1 1l3.5 3.5L1 8" fill="none" stroke="#0b6fb8" stroke-width="1.3"/></svg>
    </div>
  </article>

  <div class="card" style="left:907px;width:30px">
    <div class="abs" style="inset:0;background:linear-gradient(270deg,#fff 0%,rgba(255,255,255,.3) 100%);z-index:3"></div>
  </div>

  <div class="arrow" style="left:513px;top:514px">
    <svg width="8" height="12" viewBox="0 0 8 12"><path d="M6 1L1.5 6 6 11" fill="none" stroke="#222831" stroke-width="1.4"/></svg>
  </div>
  <div class="arrow" style="left:944px;top:514px">
    <svg width="8" height="12" viewBox="0 0 8 12"><path d="M2 1l4.5 5L2 11" fill="none" stroke="#222831" stroke-width="1.4"/></svg>
  </div>
</section>

<section class="styles">
  <div class="mode" style="left:234px;width:141px;background:linear-gradient(180deg,var(--sky),#d7dde2)" role="img" aria-label="Illustration of a learner studying online at a desk"></div>
  <div class="mode__label" style="left:234px;width:141px">Online</div>
  <div class="mode" style="left:409px;width:132px;background:linear-gradient(180deg,var(--sky),#d7dde2)" role="img" aria-label="Illustration of a teacher and a learner in a one-to-one session"></div>
  <div class="mode__label" style="left:409px;width:132px">One-to-One</div>
  <div class="mode" style="left:596px;width:83px;background:linear-gradient(180deg,#dfe4e8,#9aa3ab)" role="img" aria-label="Illustration of a monitor showing a webinar"></div>
  <div class="mode__label" style="left:596px;width:83px">Webinar</div>

  <h2 class="abs display section-title" style="left:728px;top:692px">Fit your style</h2>
  <p class="abs" style="left:728px;top:730px;font-size:15px">The way you prefer it best.</p>
</section>

<section class="cta">
  <h2 class="abs display section-title" style="left:0;width:1200px;top:829px;text-align:center">Ready to learn? <span style="color:var(--orange)">Join now!</span></h2>
  <a class="btn btn--orange" style="left:534px;top:870px;width:132px;height:28px;font-size:13px">Start today!</a>
</section>

<footer class="abs footer">
  <div class="abs brand" style="left:232px;top:83px">
    <span class="brand__dot"></span>
    <span class="brand__name">DeskWizard</span>
  </div>
  <div class="abs social" style="left:234px;top:130px" aria-label="Social media links">
    <span></span><span></span><span></span>
  </div>

  <div class="abs news__title" style="left:488px;top:78px">Let's stay connected! Opt-in our newsletter!</div>
  <div class="abs news__field" style="left:488px;top:108px">Email address</div>
  <a class="btn btn--blue" style="left:488px;top:134px;width:85px;height:20px;font-size:10px">Subscribe</a>

  <div class="abs links" style="left:821px;top:66px">
    <b>Services</b><br>Courses<br>Webinar<br>One-to-One<br>Questions
  </div>
  <div class="abs links" style="left:915px;top:66px">
    <b>Company</b><br>Blog<br>About<br>Terms<br>Contact
  </div>
</footer>

</body>
</html>
```